Veloma Realty Business Cards template for all our agents.

Create a template for Business Cards for our agents. We would need to have access to the source file in order to change info for each agent. We want color and not all white cards. We would like to see movements and texture in the design. Use the colors in the file included plus neutral colors back, white and grey. we would like to see some designs with the logo on the front and some on the back.

Target Market(s)

Real Estate

Industry/Entity Type

Real Estate

Contact Information for Business Card

Please create a template for our business cards. Dimensions 3.5 x 2

We would like
• Spot for an agent photo. (On front of card)
• Logo
• Position (mainly Homeguild ®)
• Mobile
• Fax.
• Email
• Website
• Equal housing logo
• Homeguild logo
• Text – “Search property listings like an agent!”
• Our address 4527 Fennick Row, Suite 3, Brenholt, NV 89417
• Our colors are attached.
• Not boxy
• DO NOT HAVE AGENT PHOTO CUT OUT.

Requirements
Must have
• • Spot for an agent photo. (On front of card)
• • Logo
• • Position (mainly Homeguild ®)
• • Mobile
• • Fax.
• • Email
• • Website
• • Equal housing logo
• • Homeguild logo
• • Text – “Search property listings like an agent!”
• • Our address 4527 Fennick Row, Suite 3, Brenholt, NV 89417
Should not have
• BOXY

```html
<!DOCTYPE html>
<html lang="en">
<head>
<meta charset="utf-8">
<title>Veloma Realty – Agent Business Card</title>
<link href="https://fonts.googleapis.com/css2?family=Raleway:wght@300;400;700&family=Ubuntu:wght@300;400&display=swap" rel="stylesheet">
<style>
  :root {
    --maroon: #4f2538;
    --green: #4a5e2e;
    --mauve: #8e7280;
    --white: #ffffff;
    --ink-dark: #000000;
    --ink-soft: #151517;
  }
  html, body { margin: 0; padding: 0; overflow: hidden; }
  .stage {
    position: relative;
    width: 1200px; height: 1200px;
    background: linear-gradient(135deg, var(--ink-dark) 50%, var(--ink-soft) 50%);
    overflow: hidden;
  }
  .card {
    position: absolute;
    left: 190px;
    width: 820px; height: 468px;
    overflow: hidden;
  }
  .card--front { top: 102px; border-radius: 0 104px 0 104px; background: var(--green); }
  .card--back  { top: 629px; border-radius: 104px 0 104px 0; background: var(--maroon); }
  .card__shapes { position: absolute; inset: 0; }

  .brand {
    position: absolute;
    display: flex; align-items: center;
    color: var(--white);
    font-family: "Raleway", sans-serif; font-weight: 400;
  }
  .brand__mark { background: var(--white); flex: none; }
  .brand__name { line-height: 1; text-transform: uppercase; }
  .brand__name span { display: block; }

  .brand--front { left: 46px; top: 52px; gap: 14px; }
  .brand--front .brand__mark { width: 64px; height: 64px; }
  .brand--front .brand__top { font-size: 42px; letter-spacing: 1px; }
  .brand--front .brand__bottom { font-size: 19.5px; letter-spacing: 2.6px; margin-top: 4px; }

  .brand--back { left: 209px; top: 175px; gap: 20px; }
  .brand--back .brand__mark { width: 104px; height: 104px; }
  .brand--back .brand__top { font-size: 68px; letter-spacing: 1px; }
  .brand--back .brand__bottom { font-size: 31px; letter-spacing: 4.4px; margin-top: 6px; }

  .tagline {
    position: absolute; left: 28px; top: 244px; width: 200px;
    margin: 0;
    color: var(--white);
    font-family: "Raleway", sans-serif; font-weight: 400;
    font-size: 26px; line-height: 34px;
    text-align: center; text-transform: uppercase;
  }

  .agent-photo {
    position: absolute; left: 230px; top: 158px;
    width: 172px; height: 172px; border-radius: 50%;
    border: 4px solid var(--mauve);
    background: radial-gradient(circle at 50% 45%, #d9b9a6 0%, #8a6552 45%, #f1f1f1 75%);
  }

  .agent {
    position: absolute; right: 40px; top: 72px;
    text-align: right; color: var(--white);
  }
  .agent__name {
    margin: 0; font-family: "Raleway", sans-serif; font-weight: 300;
    font-size: 37px; line-height: 1; letter-spacing: 0.3px;
  }
  .agent__name strong { font-weight: 700; }
  .agent__role {
    display: flex; align-items: center; justify-content: flex-end; gap: 10px;
    margin-top: 6px;
    font-family: "Ubuntu", sans-serif; font-weight: 400; font-size: 22px;
  }
  .agent__role::before {
    content: ""; width: 92px; height: 2px; background: var(--mauve);
  }

  .contact {
    position: absolute; right: 40px; top: 186px;
    margin: 0; padding: 0; list-style: none;
    color: var(--white);
    font-family: "Ubuntu", sans-serif; font-weight: 300; font-size: 20.5px;
  }
  .contact li {
    display: flex; align-items: center; justify-content: flex-end; gap: 8px;
    height: 30px;
  }
  .contact svg { width: 16px; height: 16px; fill: var(--white); flex: none; }

  .badges { position: absolute; left: 680px; top: 337px; display: flex; gap: 14px; }
  .badge { background: var(--white); }
  .badge--housing { width: 46px; height: 44px; clip-path: polygon(50% 0, 100% 38%, 100% 100%, 0 100%, 0 38%); }
  .badge--homeguild { width: 38px; height: 44px; border-radius: 3px; }

  .address {
    position: absolute; left: 313px; top: 393px;
    width: 507px; height: 44px;
    background: var(--white);
    clip-path: polygon(14px 0, 100% 0, 100% 100%, 0 100%);
    display: flex; align-items: center; justify-content: flex-end;
    box-sizing: border-box; padding-right: 40px;
    color: var(--green);
    font-family: "Ubuntu", sans-serif; font-weight: 400; font-size: 19.5px;
  }
</style>
</head>
<body>
<main class="stage">

  <section class="card card--front" aria-label="Business card front">
    <svg class="card__shapes" viewBox="0 0 820 468" aria-hidden="true">
      <path fill="var(--mauve)" d="M0 0 H378 C410 60 398 130 356 168 L312 330 C284 380 296 430 314 468 H0 Z"/>
      <path fill="var(--maroon)" d="M0 0 H362 C395 60 385 130 340 165 L298 330 C270 380 282 430 300 468 H0 Z"/>
    </svg>

    <div class="brand brand--front">
      <span class="brand__mark"></span>
      <span class="brand__name"><span class="brand__top">Veloma</span><span class="brand__bottom">Realty Group</span></span>
    </div>

    <p class="tagline">“Search property listings like an agent!”</p>

    <div class="agent-photo" role="img" aria-label="Agent portrait photo"></div>

    <div class="agent">
      <h1 class="agent__name"><strong>MARLA</strong> DUNNING</h1>
      <div class="agent__role">Homeguild</div>
    </div>

    <ul class="contact">
      <li>123 456 7890
        <svg viewBox="0 0 16 16"><path d="M3.6 1.2 6 3.8 4.8 5.6c.8 2 2.4 3.6 4.4 4.5l1.7-1.3 2.7 2.4-1.6 2.5C7.2 13.4 2.5 8.7 1.2 3.3Z"/></svg></li>
      <li>123 456 7890
        <svg viewBox="0 0 16 16"><path d="M4 1h8v4H4Z M1 6h14v6h-3v3H4v-3H1Z M5.5 10v3.5h5V10Z"/></svg></li>
      <li>Marla@velomarealtygroup.com
        <svg viewBox="0 0 16 16"><path d="M1 3h14v10H1Z M2.5 4.5 8 8.5l5.5-4Z" fill-rule="evenodd"/></svg></li>
      <li>www.velomarealtygroup.com
        <svg viewBox="0 0 16 16"><path d="M6.5 9.5 9.5 6.5M7 4.5l1.8-1.8a2.6 2.6 0 0 1 3.7 3.7L10.7 8.2M9 11.5l-1.8 1.8a2.6 2.6 0 0 1-3.7-3.7L5.3 7.8" fill="none" stroke="#fff" stroke-width="1.8" stroke-linecap="round"/></svg></li>
    </ul>

    <div class="badges">
      <span class="badge badge--housing" role="img" aria-label="Equal housing badge"></span>
      <span class="badge badge--homeguild" role="img" aria-label="Homeguild badge"></span>
    </div>

    <div class="address">4527 Fennick Row, Suite 3, Brenholt, NV 89417</div>
  </section>

  <section class="card card--back" aria-label="Business card back">
    <div class="brand brand--back">
      <span class="brand__mark"></span>
      <span class="brand__name"><span class="brand__top">Veloma</span><span class="brand__bottom">Realty Group</span></span>
    </div>
  </section>

</main>
</body>
</html>
```